BSC Flyer to attract applicants 11x17

Brightline Stagecraft Company provides crew for local concerts, filming, theater, and corporate events.
The flyer will be posted on bulletin boards at colleges with theater programs.
Our primary venues are historic theaters in downtown LA
Need a 11x17 poster to attract potential applicants/crew
I have attached a poster that one of our staff made that has all if the relevant info - but i know the poster can look much better than that. I have also attached many images and our logo. It is not necessary to use all of the images, or any of them. The two images of the theater interiors are the venues we operate so they would be the first to include. I can send additional info or images upon request. Thank you

Entertainment

• APPLY@BSCCREWHUB.LA

```html
<!DOCTYPE html>
<html lang="en">
<head>
<meta charset="utf-8">
<title>Brightline Stagecraft Company – Open Positions</title>
<link href="https://fonts.googleapis.com/css2?family=Roboto+Slab:wght@400;600&family=Arimo&family=Montserrat:wght@500;700&display=swap" rel="stylesheet">
<style>
  :root {
    --brand-blue: #0a4fb8;
    --ink-grey: #8a8a8a;
    --band-grey: #9a9a9a;
    --curve-grey: #a6a6a6;
    --paper: #ffffff;
  }
  * { margin: 0; padding: 0; box-sizing: border-box; }
  html, body { width: 817px; height: 1200px; overflow: hidden; background: var(--paper); }
  .flyer { position: relative; width: 817px; height: 1200px; background: var(--paper); }
  .hero { position: absolute; left: 0; top: 0; width: 817px; height: 620px; }
  .brand-tile {
    position: absolute; left: 43px; top: 42px; width: 135px; height: 103px;
    background: var(--paper); display: flex; align-items: center; justify-content: center;
    font-family: "Roboto Slab", serif; font-weight: 600; font-size: 38px; color: var(--brand-blue);
  }
  .company-name {
    position: absolute; left: 0; top: 630px; width: 817px; text-align: center;
    font-family: "Roboto Slab", serif; font-weight: 600; color: var(--brand-blue);
  }
  .company-name .main { display: block; font-size: 32px; line-height: 38px; }
  .company-name .sub { display: block; font-size: 15px; letter-spacing: 12px; line-height: 20px; margin-top: 2px; padding-left: 12px; }
  .headline {
    position: absolute; left: 57px; top: 725px; width: 705px; height: 73px;
    background: var(--brand-blue); border-radius: 11px; color: #fff;
    font-family: "Roboto Slab", serif; font-weight: 400; font-size: 52px;
    display: flex; align-items: center; justify-content: center; letter-spacing: 0.5px;
  }
  .pitch {
    position: absolute; left: 0; top: 822px; width: 817px; text-align: center;
    font-family: "Arimo", sans-serif; font-size: 36px; line-height: 45px; color: var(--ink-grey);
  }
  .apply-label {
    position: absolute; left: 0; top: 985px; width: 817px; text-align: center;
    font-family: "Montserrat", sans-serif; font-weight: 700; font-size: 42px; color: var(--brand-blue);
    text-decoration: underline; text-underline-offset: 6px; text-decoration-thickness: 3px;
  }
  .apply-email {
    position: absolute; left: 0; top: 1050px; width: 817px; text-align: center;
    font-family: "Montserrat", sans-serif; font-weight: 500; font-size: 35px; color: var(--brand-blue);
  }
  .footer-band {
    position: absolute; left: 0; top: 1121px; width: 817px; height: 57px; background: var(--band-grey);
    display: flex; align-items: center; justify-content: center;
    font-family: "Montserrat", sans-serif; font-weight: 500; font-size: 24px; letter-spacing: 2px; color: #fff;
  }
</style>
</head>
<body>
<div class="flyer">
  <svg class="hero" viewBox="0 0 817 620" xmlns="http://www.w3.org/2000/svg">
    <defs>
      <linearGradient id="hallTones" x1="0" y1="0" x2="1" y2="1">
        <stop offset="0" stop-color="#b9662a"/>
        <stop offset="0.35" stop-color="#d8883a"/>
        <stop offset="0.6" stop-color="#8a4a1e"/>
        <stop offset="0.85" stop-color="#6a1e1a"/>
        <stop offset="1" stop-color="#3a1a12"/>
      </linearGradient>
      <radialGradient id="stageTones" cx="0.5" cy="0.4" r="0.6">
        <stop offset="0" stop-color="#c7a37a"/>
        <stop offset="0.5" stop-color="#6a3a6e"/>
        <stop offset="1" stop-color="#2a1640"/>
      </radialGradient>
    </defs>
    <path d="M0 0H817V200C775 440 560 578 0 606Z" fill="var(--curve-grey)"/>
    <path role="img" aria-label="Photo of an ornate historic theater interior with gilded balconies and red stage curtain" d="M0 0H817V179C770 420 560 562 0 592Z" fill="url(#hallTones)"/>
    <circle cx="668" cy="438" r="109" fill="var(--curve-grey)"/>
    <circle role="img" aria-label="Photo of a second historic theater stage lit in purple" cx="668" cy="438" r="103" fill="url(#stageTones)"/>
  </svg>

  <div class="brand-tile">BSC</div>

  <div class="company-name">
    <span class="main">BRIGHTLINE STAGECRAFT</span>
    <span class="sub">COMPANY</span>
  </div>

  <div class="headline">HAS OPEN POSITIONS</div>

  <p class="pitch">We Are Looking For Talented<br>Technicians&nbsp; To Add To Our Roster<br>Of Skilled Professionals.</p>

  <p class="apply-label">Send Resume To:</p>
  <p class="apply-email">apply@bsccrewhub.la</p>

  <div class="footer-band">WWW.BSCCREWHUB.LA</div>
</div>
</body>
</html>
```